Our business is a Startup that Employs Caregivers to do IN HOME Care of the Elderly. Our website is not yet running. But, a business similar to ours is Cedarhaven.com

We are looking for a card that only has 4 Elements:
-Logo
- Website
- Tag Line
- Phone
We would like to see some eye catching backgrounds.
We would like to see some designs with and some without a Photo.
Would like the Photo to be of a Caregiver taking care of a Senior. The photo should show both of them smiling.

Target Market(s)

Age 35-55 who has Parents that are Elderly and need care

Industry/Entity Type

Home Health Care

Contact Information for Business Card

Want it to Pop Out to the viewer . Thinking maybe:
Side 1: LOGO with Website & Tag line
Side 2: Phone Number

Font styles to use
Other font styles liked:
• Same Font as our Logo

Colors

Designer to choose colors to be used in the design.

Requirements
Must have
• Logo, website, Tag Line, Phone number and Email: "info@brightlarkcare.com"
• Please use one of the photos that I have attached.
Nice to have
• Would like to see a Photo worked in that has a Care Taker taking care of an Elderly Person and they are both smiling.

```html
<!DOCTYPE html>
<html lang="en">
<head>
<meta charset="utf-8">
<title>BrightLark – Business Card</title>
<link rel="stylesheet" href="https://fonts.googleapis.com/css2?family=Quicksand:wght@600;700&display=swap">
<style>
  :root {
    --backdrop: #d5eaf8;
    --brand-blue: #0d56a4;
    --brand-orange: #f05a28;
    --paper: #ffffff;
    --font-main: "Quicksand", "Trebuchet MS", sans-serif;
  }
  * { box-sizing: border-box; margin: 0; padding: 0; }
  html, body {
    width: 1200px;
    height: 526px;
    overflow: hidden;
    background: var(--backdrop);
    font-family: var(--font-main);
  }
  .canvas {
    position: relative;
    width: 1200px;
    height: 526px;
  }
  .card {
    position: absolute;
    top: 127px;
    width: 455px;
    height: 284px;
    overflow: hidden;
  }

  /* Front card */
  .card--front {
    left: 127px;
    background: var(--paper);
  }
  .card--front .contact-band {
    position: absolute;
    left: 0;
    top: 142px;
    width: 100%;
    height: 142px;
    background: var(--brand-blue);
  }
  .card--front .brand-name {
    position: absolute;
    left: 21px;
    top: 30px;
    font-size: 28px;
    font-weight: 700;
    color: var(--brand-blue);
    letter-spacing: 0.2px;
  }
  .card--front .tagline {
    position: absolute;
    left: 21px;
    top: 74px;
    font-size: 13px;
    font-weight: 700;
    letter-spacing: 1.1px;
    line-height: 20px;
    color: var(--brand-blue);
  }
  .tagline .accent,
  .tagline .tagline__second { color: var(--brand-orange); }

  .brand-emblem {
    position: absolute;
    left: 285px;
    top: 45px;
    width: 168px;
    height: 168px;
    border-radius: 50%;
    background: var(--brand-orange);
  }

  .contact-list {
    position: absolute;
    left: 25px;
    top: 165px;
    list-style: none;
  }
  .contact-list li {
    display: flex;
    align-items: center;
    height: 35.5px;
    font-size: 16.5px;
    font-weight: 700;
    color: var(--paper);
  }
  .contact-list svg {
    width: 26px;
    height: 24px;
    margin-right: 17px;
    flex: none;
  }

  /* Back card */
  .card--back {
    left: 622px;
    background: var(--brand-blue);
    color: var(--paper);
    text-align: center;
  }
  .back-lockup {
    position: absolute;
    left: 0;
    top: 63px;
    width: 100%;
    display: flex;
    justify-content: center;
    align-items: center;
    gap: 10px;
  }
  .back-lockup .brand-dot {
    width: 30px;
    height: 30px;
    border-radius: 50%;
    background: var(--brand-orange);
  }
  .back-lockup .brand-name {
    font-size: 36px;
    font-weight: 700;
    color: var(--paper);
  }
  .card--back .web-address {
    position: absolute;
    left: 0;
    top: 117px;
    width: 100%;
    font-size: 18px;
    font-weight: 700;
    letter-spacing: 2.6px;
  }
  .card--back .tagline {
    position: absolute;
    left: 0;
    top: 170px;
    width: 100%;
    font-size: 17.5px;
    letter-spacing: 2.2px;
    line-height: 31px;
    color: var(--paper);
  }
</style>
</head>
<body>
<main class="canvas">

  <section class="card card--front" aria-label="Business card front">
    <div class="contact-band"></div>
    <h1 class="brand-name">BrightLark</h1>
    <p class="tagline">
      In Home <span class="accent">Care</span> for Elderly<br>
      <span class="tagline__second">Everyone Deserves it!</span>
    </p>
    <div class="brand-emblem" aria-hidden="true"></div>

    <ul class="contact-list">
      <li>
        <svg viewBox="0 0 26 24" aria-hidden="true" fill="none" stroke="var(--brand-orange)" stroke-width="2.2" stroke-linecap="round" stroke-linejoin="round">
          <path d="M5 3l4 0 2 5-3 2c1.5 3 3.5 5 6.5 6.5l2-3 5 2v4c0 1-1 2-2 2C11 21 3 13 3 5c0-1 1-2 2-2z"/>
          <path d="M15 3a8 8 0 0 1 7 7M15 7a4 4 0 0 1 3 3"/>
        </svg>
        your phone number
      </li>
      <li>
        <svg viewBox="0 0 26 24" aria-hidden="true" fill="none" stroke="var(--brand-orange)" stroke-width="2" stroke-linejoin="round">
          <rect x="2" y="5" width="22" height="15"/>
          <path d="M2 5l11 9 11-9M2 20l8-7M24 20l-8-7"/>
        </svg>
        your email
      </li>
      <li>
        <svg viewBox="0 0 26 24" aria-hidden="true" fill="none" stroke="var(--brand-orange)" stroke-width="2">
          <circle cx="13" cy="12" r="10"/>
          <ellipse cx="13" cy="12" rx="4.5" ry="10"/>
          <path d="M3 12h20M5 6.5h16M5 17.5h16"/>
        </svg>
        www.brightlarkcare.com
      </li>
    </ul>
  </section>

  <section class="card card--back" aria-label="Business card back">
    <div class="back-lockup">
      <span class="brand-dot" aria-hidden="true"></span>
      <span class="brand-name">BrightLark</span>
    </div>
    <p class="web-address">www.brightlarkcare.com</p>
    <p class="tagline">
      <strong>In Home <span class="accent">Care</span> for Elderly</strong><br>
      <strong class="tagline__second">Everyone Deserves it!</strong>
    </p>
  </section>

</main>
</body>
</html>
```